Mabel's Fitness Business Cards

I would like my business cards to look expensive and sophisticated using my logo and the information below.

FRONT
Mabel’s Fitness logo

Tag line Become your happiest, healthiest and strongest self

Mabel Quint Harlow
Personal Trainer

e. mabel@mabelsfitstudio.example

t. 0781530462

w. www.mabelsfitstudio.example

```html
<!DOCTYPE html>
<html lang="en">
<head>
<meta charset="utf-8">
<title>Mabel's Fitness Business Cards</title>
<link rel="stylesheet" href="https://fonts.googleapis.com/css2?family=Questrial&display=swap">
<style>
  :root {
    --backdrop: #d7d5d6;
    --card: #000000;
    --teal: #5fb2b6;
    --stone: #aaa3a3;
    --rule: #1c3332;
    --shadow: rgba(0,0,0,0.28);
  }
  html, body {
    margin: 0;
    width: 1200px;
    height: 1200px;
    overflow: hidden;
    background: var(--backdrop);
    font-family: "Questrial", sans-serif;
  }
  .canvas { position: relative; width: 1200px; height: 1200px; }
  .card {
    position: absolute;
    left: 180px;
    width: 840px;
    height: 480px;
    background: var(--card);
    box-shadow: 5px 5px 6px var(--shadow);
  }
  .card--front { top: 98px; }
  .card--back { top: 622px; }

  .brand {
    position: absolute;
    left: 0; right: 0;
    top: 136px;
    text-align: center;
    color: var(--teal);
  }
  .brand__mark {
    display: block;
    margin: 0 auto 8px;
    width: 56px; height: 56px;
  }
  .brand__name {
    font-size: 13px;
    letter-spacing: 0.42em;
    line-height: 1.15;
    text-transform: uppercase;
    padding-left: 0.42em;
  }

  .rule {
    position: absolute;
    left: 62px;
    width: 712px;
    height: 1px;
    background: var(--rule);
  }
  .card--front .rule { top: 310px; }
  .card--back .rule { top: 311px; left: 64px; }

  .identity {
    position: absolute;
    left: 62px;
    top: 338px;
    text-align: center;
  }
  .identity__name {
    margin: 0;
    font-weight: 400;
    font-size: 34px;
    line-height: 1;
    color: var(--teal);
    text-transform: uppercase;
    letter-spacing: -0.01em;
  }
  .identity__role {
    margin: 6px 0 0;
    font-size: 24px;
    color: var(--stone);
  }

  .contacts {
    position: absolute;
    left: 514px;
    top: 333px;
    margin: 0; padding: 0;
    list-style: none;
    font-size: 19.5px;
    line-height: 24px;
    color: var(--stone);
  }
  .contacts li { display: flex; align-items: center; gap: 5px; white-space: nowrap; }
  .contacts svg { width: 17px; height: 17px; fill: var(--teal); flex: none; }

  .tagline {
    position: absolute;
    left: 0; right: 0;
    top: 354px;
    margin: 0;
    padding-left: 62px;
    text-align: center;
    font-size: 24px;
    color: var(--stone);
    text-transform: uppercase;
    letter-spacing: -0.01em;
  }
  .tagline em { font-style: normal; color: var(--teal); }
</style>
</head>
<body>
<div class="canvas">

  <section class="card card--front">
    <div class="brand">
      <svg class="brand__mark" viewBox="0 0 56 56" aria-hidden="true">
        <circle cx="28" cy="28" r="25" fill="none" stroke="currentColor" stroke-width="3"/>
      </svg>
      <div class="brand__name">Mabel's<br>Fitness</div>
    </div>
    <div class="rule"></div>
    <div class="identity">
      <h1 class="identity__name">Mabel Quint Harlow</h1>
      <p class="identity__role">Personal Trainer</p>
    </div>
    <ul class="contacts">
      <li>
        <svg viewBox="0 0 24 24" aria-hidden="true"><path d="M6.6 10.8a15.1 15.1 0 0 0 6.6 6.6l2.2-2.2c.3-.3.7-.4 1-.2 1.1.4 2.3.6 3.6.6.6 0 1 .4 1 1V20c0 .6-.4 1-1 1A17 17 0 0 1 3 4c0-.6.4-1 1-1h3.5c.6 0 1 .4 1 1 0 1.3.2 2.5.6 3.6.1.3 0 .7-.2 1z"/></svg>
        0781530462
      </li>
      <li>
        <svg viewBox="0 0 24 24" aria-hidden="true"><path d="M2 5h20v2l-10 6L2 7z"/><path d="M2 9l10 6 10-6v10H2z"/></svg>
        mabel@mabelsfitstudio.example
      </li>
      <li>
        <svg viewBox="0 0 24 24" aria-hidden="true"><circle cx="12" cy="12" r="10"/></svg>
        www.mabelsfitstudio.example
      </li>
    </ul>
  </section>

  <section class="card card--back">
    <div class="brand">
      <svg class="brand__mark" viewBox="0 0 56 56" aria-hidden="true">
        <circle cx="28" cy="28" r="25" fill="none" stroke="currentColor" stroke-width="3"/>
      </svg>
      <div class="brand__name">Mabel's<br>Fitness</div>
    </div>
    <div class="rule"></div>
    <p class="tagline">Become your <em>happiest, healthiest</em> and <em>strongest self</em></p>
  </section>

</div>
</body>
</html>
```